Design a business card for Brenton's Heat Guardian
Brenton's Heat Guardian
Design a business card for Brenton's Heat Guardian - Food
Creative Brief
Traditional
Hal Brenton
President and CEO
52894 Corvane Lane Clinton Township, MI 48052
hbrenton2261@mailvex.example
www.brentonsheatguardian.example
Simple color marks, with some white space to write notes

```html
<!DOCTYPE html>
<html lang="en">
<head>
<meta charset="utf-8">
<title>Brenton's Heat Guardian — Business Card</title>
<link href="https://fonts.googleapis.com/css2?family=Open+Sans:wght@400;600;700&display=swap" rel="stylesheet">
<style>
  :root {
    --backdrop: #e6e6e6;
    --card-white: #ffffff;
    --card-black: #1c1c1c;
    --ink: #1a1a1a;
    --ink-light: #e8e8e8;
    --ink-muted: #b5b5b5;
    --accent-orange: #f26a1b;
    --accent-red: #d6321f;
    --accent-yellow: #f7c51e;
    --divider: #4a4a4a;
  }
  * { margin: 0; padding: 0; box-sizing: border-box; }
  html, body {
    width: 1200px; height: 908px; overflow: hidden;
    background: var(--backdrop);
    font-family: "Open Sans", Arial, sans-serif;
  }
  .stage {
    width: 1200px; height: 908px;
    display: flex; align-items: center; justify-content: center; gap: 40px;
  }
  .card {
    position: relative;
    width: 540px; height: 309px;
    border-radius: 18px;
    overflow: hidden;
    background: var(--card-white);
    box-shadow: 0 6px 18px rgba(0,0,0,0.12);
  }
  .brand { display: flex; align-items: center; gap: 10px; }
  .brand-mark { width: 12px; height: 12px; background: var(--accent-orange); flex: none; }
  .brand-name { font-weight: 700; color: var(--ink); line-height: 1.05; }

  /* Front */
  .card-front .brand { position: absolute; left: 42px; bottom: 40px; }
  .card-front .brand-name { font-size: 26px; }

  /* Back */
  .card-back .upper {
    position: absolute; left: 0; top: 0; right: 0; height: 172px;
    display: flex; align-items: center; justify-content: center;
  }
  .card-back .brand-name { font-size: 24px; }
  .stripes { position: absolute; left: 0; top: 172px; width: 540px; height: 8px; }
  .lower {
    position: absolute; left: 0; top: 180px; right: 0; bottom: 0;
    background: var(--card-black);
    display: flex;
  }
  .person {
    width: 230px; padding: 22px 0 0 42px;
    border-right: 1px solid var(--divider);
    margin: 18px 0;
  }
  .person-name { color: var(--ink-light); font-size: 19px; font-weight: 600; }
  .person-title { color: var(--accent-orange); font-size: 12px; margin-top: 4px; }
  .contacts {
    list-style: none; padding: 16px 0 0 22px;
    color: var(--ink-muted); font-size: 10.5px; line-height: 1.55;
  }
  .contacts li { display: flex; align-items: center; gap: 7px; white-space: nowrap; }
  .contacts svg { width: 10px; height: 10px; flex: none; }
</style>
</head>
<body>
<main class="stage">

  <section class="card card-front" aria-label="Card front">
    <div class="brand">
      <span class="brand-mark"></span>
      <span class="brand-name">Brenton's<br>Heat Guardian</span>
    </div>
  </section>

  <section class="card card-back" aria-label="Card back">
    <div class="upper">
      <div class="brand">
        <span class="brand-mark"></span>
        <span class="brand-name">Brenton's<br>Heat Guardian</span>
      </div>
    </div>

    <svg class="stripes" viewBox="0 0 540 8" preserveAspectRatio="none" aria-hidden="true">
      <rect x="0" y="0" width="540" height="2" fill="var(--accent-red)"/>
      <rect x="0" y="3" width="540" height="2" fill="var(--accent-orange)"/>
      <rect x="0" y="6" width="540" height="2" fill="var(--accent-yellow)"/>
    </svg>

    <div class="lower">
      <div class="person">
        <p class="person-name">Hal Brenton</p>
        <p class="person-title">President and CEO</p>
      </div>
      <ul class="contacts">
        <li>
          <svg viewBox="0 0 10 10"><path d="M5 0.5a3 3 0 0 1 3 3c0 2.3-3 6-3 6s-3-3.7-3-6a3 3 0 0 1 3-3z" fill="var(--accent-orange)"/><circle cx="5" cy="3.5" r="1" fill="var(--card-black)"/></svg>
          52894 Corvane Lane Fernbrook Township, MI 48052
        </li>
        <li>
          <svg viewBox="0 0 10 10"><path d="M2 1l2 0.4 0.6 2-1.2 1a6 6 0 0 0 2.2 2.2l1-1.2 2 0.6L9 8l-1 1C4.5 9 1 5.5 1 2z" fill="var(--accent-orange)"/></svg>
          586-555-0142
        </li>
        <li>
          <svg viewBox="0 0 10 10"><path d="M2 1l2 0.4 0.6 2-1.2 1a6 6 0 0 0 2.2 2.2l1-1.2 2 0.6L9 8l-1 1C4.5 9 1 5.5 1 2z" fill="var(--accent-orange)"/></svg>
          248-555-0187
        </li>
        <li>
          <svg viewBox="0 0 10 10"><rect x="0.5" y="2" width="9" height="6" fill="var(--accent-orange)"/><path d="M0.5 2l4.5 3.5L9.5 2" stroke="var(--card-black)" stroke-width="0.8" fill="none"/></svg>
          hbrenton2261@mailvex.example
        </li>
        <li>
          <svg viewBox="0 0 10 10"><circle cx="5" cy="5" r="4.3" fill="var(--accent-orange)"/><circle cx="5" cy="5" r="1.4" fill="var(--card-black)"/></svg>
          halbrenton.heat
        </li>
        <li>
          <svg viewBox="0 0 10 10"><circle cx="5" cy="5" r="4.2" fill="none" stroke="var(--accent-orange)" stroke-width="1"/><path d="M1 5h8M5 1c-2 2.5-2 5.5 0 8M5 1c2 2.5 2 5.5 0 8" stroke="var(--accent-orange)" stroke-width="0.8" fill="none"/></svg>
          www.brentonsheatguardian.example
        </li>
      </ul>
    </div>
  </section>

</main>
</body>
</html>
```